Tradeshow Banner Stand - 36" x 80

Create design for a new banner i will order.
- Training on how to "add on" Christmas Light Installation to your current Service Business.

at https://brightenyourseasonplan.example/live

sorry but my GM wants it to have these items- and be more simple (not so busy)

ATTN: LANDSCAPERS
Is Your Winter
Revenue Down?

Add On Christmas Light Install
with Lumavexa’s FREE Training

Benefits:
• Grow Winter Revenue
• High Profit Margin (30% plus)
• High Growth Industry
• Avoid Off-Season Layoffs
• Use Cashflow to Grow Biz

Learn More at www.LumavexaGlow.example – QR?

```html
<!DOCTYPE html>
<html lang="en">
<head>
<meta charset="utf-8">
<title>Holiday Light Add-On Training – Roll-up Banner</title>
<link rel="stylesheet" href="https://fonts.googleapis.com/css2?family=League+Gothic&family=Oswald:wght@500&display=swap">
<style>
  :root {
    --page-bg: #d9dad6;
    --banner-black: #000000;
    --gold: #c9a23a;
    --white: #ffffff;
    --red: #ee0000;
    --ink: #111111;
    --photo-dark: #1d1f19;
    --photo-warm: #6b4a22;
    --photo-glow: #d9a552;
  }
  * { margin: 0; padding: 0; box-sizing: border-box; }
  html, body {
    width: 1200px; height: 1200px; overflow: hidden;
    background: var(--page-bg);
  }
  .banner {
    position: absolute; left: 340px; top: 20px;
    width: 520px; height: 1160px;
    background: var(--banner-black);
    overflow: hidden;
    font-family: "League Gothic", "Oswald", sans-serif;
    color: var(--white);
    text-transform: uppercase;
  }
  .hero-photo {
    position: absolute; left: 0; top: 0; width: 520px; height: 480px;
    background:
      radial-gradient(ellipse 60% 35% at 50% 55%, var(--photo-glow) 0%, var(--photo-warm) 45%, transparent 80%),
      linear-gradient(180deg, var(--photo-dark) 0%, #3a2c1a 55%, #6a5228 85%, var(--photo-dark) 100%);
  }
  .roof-frame { position: absolute; left: 0; top: 0; width: 520px; height: 1160px; }
  .content {
    position: absolute; left: 0; top: 382px; width: 520px;
    display: flex; flex-direction: column; align-items: center;
  }
  .presenter {
    font-family: "Oswald", sans-serif; font-weight: 500;
    text-transform: none; font-size: 22px; line-height: 1.2;
    margin-bottom: 6px;
  }
  .attention {
    color: var(--gold); font-size: 50px; line-height: 1; letter-spacing: 0.5px;
  }
  .headline {
    text-align: center; line-height: 0.92; margin-top: 6px;
  }
  .headline span { display: block; font-size: 86px; }
  .headline .accent {
    color: var(--red);
    border-bottom: 6px solid var(--red);
    padding-bottom: 2px;
  }
  .offer-box {
    margin-top: 18px; background: var(--gold); padding: 6px;
  }
  .offer-box-inner {
    border: 2px dotted var(--ink); color: var(--ink);
    font-size: 36px; line-height: 0.95; padding: 6px 16px 4px;
    text-align: center;
  }
  .benefits { margin-top: 18px; width: 400px; }
  .benefits-title { color: var(--gold); font-size: 38px; line-height: 1.05; }
  .benefits-list { list-style: none; }
  .benefits-list li {
    font-size: 34px; line-height: 1.12;
    display: flex; align-items: center;
  }
  .benefits-list li::before {
    content: ""; width: 12px; height: 12px; background: var(--gold);
    margin-right: 14px; flex: none;
  }
  .learn-band {
    position: absolute; left: 0; bottom: 0; width: 520px; height: 140px;
    background: var(--gold); color: var(--ink);
    display: flex; align-items: center; justify-content: space-between;
    padding: 0 26px 0 30px;
  }
  .learn-text { line-height: 1; }
  .learn-label { font-size: 30px; }
  .learn-url { font-size: 38px; text-transform: none; }
  .learn-sub { font-size: 22px; margin-top: 6px; text-transform: none; }
  .qr-slot {
    width: 104px; height: 104px; background: var(--white);
    border: 4px solid var(--ink); flex: none;
  }
</style>
</head>
<body>
  <main class="banner">
    <div class="hero-photo" role="img" aria-label="Photo of a large brick house at night outlined with warm white holiday lights and wreaths"></div>

    <svg class="roof-frame" viewBox="0 0 520 1160" aria-hidden="true">
      <polygon points="0,440 260,236 520,440 520,1160 0,1160" fill="var(--gold)"/>
      <polygon points="0,480 260,276 520,480 520,1160 0,1160" fill="var(--banner-black)"/>
    </svg>

    <section class="content">
      <p class="presenter">Lumavexa Lights Presents...</p>
      <p class="attention">Attn: Landscapers</p>
      <h1 class="headline">
        <span>Is your winter</span>
        <span class="accent">revenue down?</span>
      </h1>
      <div class="offer-box">
        <p class="offer-box-inner">Add on Christmas light install<br>with Lumavexa’s FREE training</p>
      </div>
      <div class="benefits">
        <p class="benefits-title">Benefits:</p>
        <ul class="benefits-list">
          <li>Grow winter revenue</li>
          <li>High profit margin (30% plus)</li>
          <li>High growth industry</li>
          <li>Avoid off-season layoffs</li>
          <li>Use cashflow to grow biz</li>
        </ul>
      </div>
    </section>

    <footer class="learn-band">
      <div class="learn-text">
        <p class="learn-label">Learn more at</p>
        <p class="learn-url">www.LumavexaGlow.example</p>
        <p class="learn-sub">brightenyourseasonplan.example/live</p>
      </div>
      <div class="qr-slot" role="img" aria-label="QR code linking to the training sign-up page"></div>
    </footer>
  </main>
</body>
</html>
```